Architectural and Engineering Firm of 50 Years Looking for Trade Show Booth Banner Design

Our Architectural and Engineering firm has been servicing the K-12 school market here in Northern and Central Indiana for the last 50 years. We need to dress up our trade show booth with some quick pull-up banner designs, and need some assistance with three banners that show some of our project portfolio, as well as a quick description of our Architectural and Engineering Services. You can find project photos in our Project Portfolio portion of our website at www.hollisprattenward.com as well as a bullet point style list of services for both our Architectural and Engineering Services. Our idea would be to have a middle banner that would have our logo and some project photos, and then have one banner that highlights our "Architectural Services" we offer, and a third banner that would highlight our "Engineering Services".

Target Market(s)

K-12 School Superintendents and Business Managers across State of Indiana

Industry/Entity Type

Architectural

Colors

Designer to choose colors to be used in the design.

Requirements
Must have
• Our company logo, descriptions of Architectural and Engineering Services we offer, project portfolio photos from our website portfolio.
Should not have
• Generic graphics of projects that aren't our work or photos of staff.

```html
<!DOCTYPE html>
<html lang="en">
<head>
<meta charset="utf-8">
<title>Hollis Pratten Ward — K-12 Banner</title>
<link rel="stylesheet" href="https://fonts.googleapis.com/css2?family=Source+Sans+3:wght@400;600;700;800&display=swap">
<style>
  :root {
    --navy: #2d4a5e;
    --navy-dark: #263f51;
    --sky: #d9ebf6;
    --sky-soft: #eaf4fa;
    --grey-shape: #e6e8e9;
    --text: #3a3f44;
    --bullet: #6b7075;
    --paper: #ffffff;
  }
  * { margin: 0; padding: 0; box-sizing: border-box; }
  html, body { width: 1200px; height: 2579px; overflow: hidden; background: var(--paper); }
  body { font-family: "Source Sans 3", sans-serif; color: var(--text); }
  .banner { position: relative; width: 1200px; height: 2579px; overflow: hidden; background: var(--paper); }
  .banner-art { position: absolute; inset: 0; width: 1200px; height: 2579px; }

  .brand { position: absolute; top: 132px; right: 68px; display: flex; align-items: center; gap: 20px; color: var(--navy); font-weight: 700; font-size: 62px; line-height: 1; }
  .brand-mark { width: 40px; height: 40px; background: var(--navy); flex: none; }

  .headline { position: absolute; top: 262px; right: 68px; text-align: right; color: var(--navy); font-weight: 800; font-size: 76px; line-height: 73px; letter-spacing: 1px; text-transform: uppercase; }

  .services { position: absolute; left: 143px; right: 60px; }
  .services-arch { top: 1685px; }
  .services-eng { top: 2064px; }
  .services h2 { color: var(--navy); font-weight: 800; font-size: 70px; line-height: 76px; letter-spacing: 0.5px; text-transform: uppercase; }
  .services ul { list-style: none; margin-top: 8px; }
  .services li { position: relative; padding-left: 34px; font-size: 30px; line-height: 36.6px; color: var(--text); }
  .services li::before { content: ""; position: absolute; left: 4px; top: 12px; width: 15px; height: 15px; border-radius: 50%; background: var(--bullet); }

  .contact { position: absolute; right: 86px; top: 2452px; text-align: right; color: var(--navy); font-weight: 700; font-size: 40px; line-height: 46px; }
</style>
</head>
<body>
<main class="banner">
  <svg class="banner-art" viewBox="0 0 520 1320" preserveAspectRatio="none">
    <path d="M0,240 Q40,420 200,460 L0,470 Z" fill="var(--sky)"/>
    <path d="M0,0 L40,0 Q40,300 250,395 Q380,440 520,405 L520,418 Q380,450 260,430 Q150,470 80,440 Q10,400 0,300 Z" fill="var(--navy)"/>
    <path d="M60,0 L68,0 Q70,260 300,360" fill="none" stroke="var(--navy)" stroke-width="3"/>

    <g fill="none" stroke="var(--navy-dark)" stroke-width="3">
      <polyline points="265,245 420,400"/>
      <polyline points="410,540 530,420"/>
      <polyline points="265,855 415,705"/>
      <polyline points="405,700 530,575"/>
    </g>

    <g role="img" aria-label="Project photo: bright school corridor with vaulted ceiling and glass entry">
      <polygon points="260,255 405,400 260,545 115,400" fill="#d8cbb6" stroke="#fff" stroke-width="4"/>
    </g>
    <g role="img" aria-label="Project photo: brick intermediate school entrance under blue sky">
      <polygon points="125,405 255,550 125,695 -20,550" fill="#a98a78" stroke="#fff" stroke-width="4"/>
    </g>
    <g role="img" aria-label="Project photo: school office reception with staff desks">
      <polygon points="395,405 525,550 395,695 265,550" fill="#b9ab98" stroke="#fff" stroke-width="4"/>
    </g>
    <g role="img" aria-label="Project photo: classroom with student desks and whiteboards">
      <polygon points="260,555 405,700 260,850 115,700" fill="#c3b7a7" stroke="#fff" stroke-width="4"/>
    </g>

    <path d="M0,1240 Q260,1200 520,1180 L520,1320 L0,1320 Z" fill="var(--sky-soft)"/>
    <path d="M60,1320 Q300,1230 520,1225 L520,1320 Z" fill="var(--sky)"/>
    <path d="M0,1215 L70,1285 L0,1290 Z" fill="var(--grey-shape)"/>
  </svg>

  <header class="brand">
    <span class="brand-mark"></span>
    <span class="brand-name">Hollis Pratten Ward</span>
  </header>

  <h1 class="headline">Actively Involved<br>with K-12 Education<br>Community</h1>

  <section class="services services-arch">
    <h2>Architectural Services</h2>
    <ul>
      <li>Building Planning &amp; Design</li>
      <li>Environmentally Conscious (LEED) Planning &amp; Design</li>
      <li>Budget Analysis and Cost Estimating</li>
      <li>Staff Input Collection &amp; Integration of Ideas</li>
      <li>Interior Design &amp; Color / Material Selection</li>
      <li>Space Planning &amp; Furniture Selection Advisement</li>
      <li>Value Engineering for Greatest Value to Taxpayers</li>
      <li>Historical Building Analysis and Planning</li>
    </ul>
  </section>

  <section class="services services-eng">
    <h2>Engineering Services</h2>
    <ul>
      <li>Mechanical Systems (HVAC &amp; Plumbing) Design</li>
      <li>Electrical Systems (Power &amp; Lighting) Design</li>
      <li>Technology Systems (Data Infrastructure &amp; Interface) Design</li>
      <li>Security Systems (Alarm, CCTV &amp; Door Access) Design</li>
      <li>Structural Systems Design &amp; Engineering</li>
      <li>Civil (Roadways, Drainage &amp; Utility) Design</li>
    </ul>
  </section>

  <footer class="contact">
    <div>Tel: (260) 555 0142</div>
    <div>inquiry@hollisprattenward.com</div>
  </footer>
</main>
</body>
</html>
```